Personal development products that change your life

This is a direct selling business that sells personal development courses, but also sells the business as well if desired. This is not MLM, and there is no handling of the product required, nor hassling friends or family. We are looking for business minded people wanting to work their own hours and achieve a desirable income from this. A success image or happy image on a flyer would be great. I'd like the website address to be displayed as well thanks. www.gainpath-hub.com.au

Target Market(s)

Business-minded individuals searching for more finances. Self motivated, driven, interested in self development.

Industry/Entity Type

Business

Font styles to use
Sans Serif

Requirements
Must have
• Are you looking for
• - a franchise or business?
• - a change of career?
• - a back up income?
• Not MLM
• No product handling or shipping
• No hard sales required
• website: www.gainpath-hub.com.au
Nice to have
• A picture or background of excited person jumping in the air, or some similar.
• Worded to enrol people interested in achieving more financial headway, or flexible hours, or travel and do this business from anywhere in the world.
• Only need access to a phone, internet connection and a desire to succeed.

```html
<!DOCTYPE html>
<html lang="en">
<head>
<meta charset="utf-8">
<title>Financial Freedom Flyer</title>
<link href="https://fonts.googleapis.com/css2?family=Noto+Serif:wght@400;700&display=swap" rel="stylesheet">
<style>
  :root {
    --backdrop: #e4e4e6;
    --paper: #ffffff;
    --navy: #2f4a66;
    --slate: #3c5773;
    --sky: #6fb0e6;
    --sky-text: #5b9fd6;
    --photo-light: #eef3f7;
    --photo-mid: #c9d3dc;
    --suit: #2a2d33;
  }
  * { margin: 0; padding: 0; box-sizing: border-box; }
  html, body {
    width: 1200px;
    height: 781px;
    overflow: hidden;
    background: var(--backdrop);
    font-family: "Noto Serif", serif;
  }
  .flyer {
    position: absolute;
    left: 330px;
    top: 10px;
    width: 540px;
    height: 760px;
    background: var(--paper);
    overflow: hidden;
    box-shadow: 0 4px 14px rgba(0,0,0,0.25);
  }
  .hero-photo {
    position: absolute;
    left: 0; top: 0;
    width: 540px; height: 350px;
    background: linear-gradient(160deg, var(--photo-light) 0%, var(--photo-mid) 55%, var(--suit) 100%);
  }
  .bands { position: absolute; left: 0; top: 0; }
  .headline {
    position: absolute;
    left: 250px; top: 58px;
    width: 220px;
    text-align: center;
    color: var(--slate);
    font-weight: 700;
    font-size: 26px;
    line-height: 1.12;
    letter-spacing: 0.5px;
  }
  .jump-photo {
    position: absolute;
    left: 300px; top: 455px;
    width: 225px; height: 250px;
    background: radial-gradient(ellipse at 50% 55%, #6d6f74 0%, #b9bcc1 45%, var(--paper) 75%);
  }
  .site-top {
    position: absolute;
    left: 26px; top: 350px;
    color: var(--sky-text);
    font-weight: 700;
    font-size: 22px;
  }
  .question {
    position: absolute;
    left: 26px; top: 382px;
    color: var(--navy);
    font-weight: 700;
    font-size: 19px;
  }
  .needs-title {
    position: absolute;
    right: 70px; top: 412px;
    color: var(--navy);
    font-weight: 700;
    font-size: 19px;
  }
  .needs-list {
    position: absolute;
    left: 26px; top: 444px;
    color: var(--sky-text);
    font-weight: 700;
    font-size: 15px;
  }
  .benefits {
    position: absolute;
    left: 48px; top: 500px;
    list-style: disc;
    color: var(--sky-text);
    font-weight: 700;
    font-size: 15px;
    line-height: 1.5;
  }
  .cta {
    position: absolute;
    left: 0; width: 400px; top: 668px;
    text-align: center;
    color: var(--navy);
    font-weight: 700;
    font-size: 21px;
  }
  .site-bottom {
    position: absolute;
    left: 0; width: 400px; top: 702px;
    text-align: center;
    color: var(--sky-text);
    font-weight: 700;
    font-size: 18px;
  }
</style>
</head>
<body>
  <main class="flyer">
    <div class="hero-photo" role="img" aria-label="Excited businessman in a suit celebrating at his laptop"></div>
    <svg class="bands" width="540" height="760" viewBox="0 0 540 760" aria-hidden="true">
      <path d="M0 0 H540 V0 Q300 8 0 46 Z" fill="var(--paper)"/>
      <path d="M0 46 Q300 8 540 0" fill="none" stroke="var(--sky)" stroke-width="7"/>
      <path d="M0 38 Q300 0 540 -8" fill="none" stroke="var(--navy)" stroke-width="9"/>
      <path d="M0 360 Q250 300 540 262 V760 H0 Z" fill="var(--paper)"/>
      <path d="M0 352 Q250 292 540 254" fill="none" stroke="var(--navy)" stroke-width="6"/>
      <path d="M0 362 Q250 302 540 264" fill="none" stroke="var(--sky)" stroke-width="8"/>
    </svg>
    <h1 class="headline">NEED MORE<br>FINANCIAL<br>FREEDOM?</h1>
    <div class="jump-photo" role="img" aria-label="Joyful businesswoman jumping in the air"></div>
    <p class="site-top">www.gainpath-hub.com.au</p>
    <p class="question">Are you looking for a franchise or business?</p>
    <p class="needs-title">You only need 3 things:</p>
    <p class="needs-list">A phone • An internet connection • A desire to succeed</p>
    <ul class="benefits">
      <li>Need a change of career?</li>
      <li>Need a back up income?</li>
      <li>Not MLM</li>
      <li>No product handling or shipping</li>
      <li>No hard sales required</li>
      <li>Set your own hours</li>
      <li>Work on this business anywhere</li>
    </ul>
    <p class="cta">Find out how</p>
    <p class="site-bottom">www.gainpath-hub.com.au</p>
  </main>
</body>
</html>
```